Gym Poster to advertise for our chiropractic business

We are needing a poster for a gym. They are a weight training gym, Copperline Gym. The poster will be 4 ft by 8 ft. This poster will be used for advertising purposes.
Target Market(s)
Athletes, 25 to 45,Men and Women,
Industry/Entity Type
Advertising
Font styles to use
Serif
Sans Serif

```html
<!DOCTYPE html>
<html lang="en">
<head>
<meta charset="utf-8">
<title>The Spine Works Chiropractic LLC – Copperline Gym Poster</title>
<link rel="stylesheet" href="https://fonts.googleapis.com/css2?family=Questrial&family=Tinos&display=swap">
<style>
  :root {
    --sky-light: #f4fbfe;
    --sky-mid: #a9dcec;
    --sky-deep: #2f97bb;
    --sky-edge: #5fb6d3;
    --brand-navy: #1f3550;
    --text-dark: #101820;
  }
  html, body {
    margin: 0;
    padding: 0;
    width: 1200px;
    height: 2400px;
    overflow: hidden;
    background: #ffffff;
  }
  .poster {
    position: relative;
    width: 1200px;
    height: 2400px;
    overflow: hidden;
  }
  .sky-backdrop {
    position: absolute;
    inset: 0;
    background:
      radial-gradient(ellipse 520px 420px at 78% 12%, rgba(255,255,255,0.95), rgba(255,255,255,0) 70%),
      radial-gradient(ellipse 700px 600px at 45% 48%, rgba(255,255,255,0.85), rgba(255,255,255,0) 75%),
      radial-gradient(ellipse 500px 500px at 10% 62%, rgba(255,255,255,0.6), rgba(255,255,255,0) 70%),
      linear-gradient(180deg, var(--sky-edge) 0%, var(--sky-mid) 30%, var(--sky-light) 50%, var(--sky-mid) 72%, var(--sky-deep) 100%);
  }
  .brand {
    position: absolute;
    top: 150px;
    left: 0;
    width: 100%;
    text-align: center;
    font-family: "Questrial", "Helvetica Neue", Arial, sans-serif;
    color: var(--brand-navy);
    font-weight: 400;
  }
  .brand-dot {
    display: block;
    width: 110px;
    height: 110px;
    margin: 0 auto 120px;
    border-radius: 50%;
    background: var(--brand-navy);
  }
  .brand-name {
    margin: 0;
    font-weight: 400;
    line-height: 1.05;
  }
  .brand-name .line-small { display: block; font-size: 104px; }
  .brand-name .line-large { display: block; font-size: 150px; }
  .services {
    position: absolute;
    top: 1080px;
    left: 0;
    width: 100%;
    margin: 0;
    padding: 0;
    list-style: none;
    text-align: center;
    font-family: "Tinos", "Times New Roman", serif;
    font-size: 58px;
    line-height: 84px;
    color: var(--text-dark);
  }
  .website {
    position: absolute;
    top: 2110px;
    left: 0;
    width: 100%;
    text-align: center;
    font-family: "Questrial", "Helvetica Neue", Arial, sans-serif;
    font-size: 86px;
    color: var(--text-dark);
  }
</style>
</head>
<body>
  <main class="poster">
    <div class="sky-backdrop" role="img" aria-label="Soft bright blue sky with light clouds and sparkles"></div>

    <header class="brand">
      <span class="brand-dot" aria-hidden="true"></span>
      <h1 class="brand-name">
        <span class="line-small">The</span>
        <span class="line-large">Spine Works</span>
        <span class="line-small">Chiropractic LLC</span>
      </h1>
    </header>

    <ul class="services">
      <li>Chiropractic Adjusting</li>
      <li>Massage Therapy</li>
      <li>Supplementation</li>
      <li>Strapping</li>
      <li>Orthotics and Bracing</li>
      <li>Sports Taping</li>
      <li>Rehabilitation Services</li>
      <li>Spinal Curve Correction</li>
      <li>Myofascial Release</li>
      <li>Comprehensive Examinations</li>
      <li>Event/Corporate Chair Massage</li>
    </ul>

    <p class="website">Alignwellclinic.com</p>
  </main>
</body>
</html>
```